organic, healthy living website needs a new home page!

We need a home page for the front page of our website (www.saffronmeadowlark.com.au).

We want to see the following at a glance! We want to gain trust - communicate value, and navigate visitors to the next step - purchasing!

Our two main products:
- certified organic veggies (weekly in Melbourne, Australia - Mentone, Frankston and Ringwood with more pick up locations to come soon)

-ethical wooden toys (by membership only at this stage - run quarterly as a bulk buy - just for Melbourne people!)

Other products:
- health appliances - juicers, dehydrators and water filters (free delivery to their door all over Australia)

- natural parenting products which promote breastfeeding, homebirth, cosleeping and gentle parenting (books, jewellery, gifts, blessingway etc) all over Australia - send via Koala Parcel.

This website holds all of our products for purchase. We want to emphasise exactly what is to offer here. We will have an info blog which we want to link THROUGH the product homepage of SM. The blog will include a directory of natural services (for a very niche market), recipes, stories, and a wealth of information to do with natural pregnancy, health, parenting, health and community!

We have 5 images linked below - we need these to correspond with the words PREGNANCY, BIRTH, PARENTING, HEALTH, And COMMUNITY and maybe a little design on these - such as dragonflies or flowers - or both. We will code these to work in a slideshow, and link to our blog.

We want this page to feature everything we do, but also be aesthetically pleasing without overkill. We want it to reflect our style, and vision. Natural, organic, and as close to nature as possible. Flow is important, as is consistency throughout the page. WE want it to appeal to our hippy mamas and papas who just want to love their babies, live organically and as healthy as they can.

We love the look and feel of the following websites:

http://thebrightlarderapp.com/

Thank you!!
Updates

Target Market(s)

20-50 year old parents who are environmentally aware and health conscious. They have very close bonds to their children.
Think bohemian, rustic, vintage yet with a modern feel.

Industry/Entity Type

Health

Font styles to use
Script

Colors
e34197
6b449b
33a6d7
0455a3
33b7a4

Requirements
Must have
• Must be clean and say at a glance exactly what we do.

```html
<!DOCTYPE html>
<html lang="en">
<head>
<meta charset="utf-8">
<title>Saffron Meadowlark – Organic Living</title>
<link href="https://fonts.googleapis.com/css2?family=Delius&family=Itim&display=swap" rel="stylesheet">
<style>
:root{
  --pink:#e34197;
  --purple:#6b449b;
  --sky:#33a6d7;
  --navy:#0455a3;
  --teal:#33b7a4;
  --ink:#222;
  --grey:#666;
  --line:#e6e6e6;
  --bar:#444;
  --shade:rgba(20,20,20,.72);
}
*{box-sizing:border-box;margin:0;padding:0}
html,body{width:1111px;height:1200px;overflow:hidden;background:#fff}
body{position:relative;font-family:"Delius",cursive;color:var(--ink)}
.abs{position:absolute}

/* header */
.brand{left:207px;top:30px;display:flex;align-items:center;gap:10px}
.brand-dot{width:38px;height:38px;border-radius:50%;background:var(--purple)}
.brand-name{font-size:21px;color:var(--purple);letter-spacing:.3px}
.order{left:689px;top:28px;width:110px;border-top:1px solid #444;border-bottom:1px solid #444;padding:3px 10px;font-size:10px;line-height:16px;color:var(--grey)}
.order b{display:block;font-weight:400;color:var(--pink)}
.badge24{left:765px;top:30px;width:32px;height:32px;border:2px solid #444;border-radius:50%;font-size:11px;display:flex;align-items:center;justify-content:center;background:#fff;color:#333}
.account{left:826px;top:34px;text-align:right;font-size:11px;line-height:16px;color:#333}
.account span{color:#999;display:block}
.cart{left:873px;top:22px}

/* hero */
.hero{left:0;top:93px;width:1111px;height:363px;background:linear-gradient(100deg,#e9e07a 0%,#cfd05a 18%,#e6a248 40%,#d6542c 60%,#b9412a 80%,#8c3a23 100%)}
.nav{left:207px;top:93px;width:697px;height:38px;background:rgba(255,255,255,.85);display:flex;align-items:center;padding:0 16px;gap:31px;font-size:15px;color:#333}
.nav .on{background:var(--sky);color:#fff;padding:2px 7px}
.search{left:872px;top:100px;width:25px;height:25px;background:var(--sky)}
.halo{left:216px;top:160px;width:260px;height:260px;border-radius:50%;background:rgba(255,255,255,.35)}
.bubble{left:225px;top:169px;width:242px;height:242px;border-radius:50%;background:#fff;text-align:center;padding-top:32px}
.bubble p{font-size:13px;line-height:24px}
.bubble .tags{font-size:15px;margin-top:2px}
.more{display:inline-block;margin-top:12px;background:var(--pink);color:#fff;font-size:10.5px;padding:7px 10px;border:1px solid #c92d80}
.dots{margin-top:16px;display:flex;justify-content:center;gap:3px}
.dots i{width:7px;height:7px;border-radius:50%;border:1px solid var(--pink)}
.dots i:first-child{background:var(--pink)}
.arrow{width:42px;height:42px;border-radius:50%;display:flex;align-items:center;justify-content:center}
.prev{left:12px;top:253px;background:#fff}
.next{left:1057px;top:253px;background:var(--pink)}

/* tiles */
.tile{top:478px;width:223px;height:152px;display:flex;align-items:center;justify-content:center;font-size:21px}
.tile .label{padding:12px 14px;background:rgba(255,255,255,.55);color:#111}
.t1{left:207px;background:linear-gradient(135deg,#e86aae,#d9428f);color:#fff}
.t2{left:444px;background:linear-gradient(135deg,#9a8f84,#d8d2c8 50%,#b33 100%)}
.t3{left:681px;background:linear-gradient(135deg,#6b4a22,#d89a3c 50%,#9c6c2c)}

.section-title{left:206px;top:645px;font-size:28px;font-family:"Itim",cursive;font-weight:400}

/* cards */
.card{overflow:hidden;box-shadow:0 5px 6px -3px rgba(0,0,0,.3)}
.card .cap{position:absolute;left:0;right:0;bottom:0;height:34px;background:var(--shade);color:#fff;font-size:20px;padding-left:14px;display:flex;align-items:center;justify-content:space-between;padding-right:10px}
.big{top:686px;width:335px;height:148px}
.c1{left:207px;background:linear-gradient(120deg,#c23a2a,#e28a2a 30%,#4f9a2c 55%,#b5242f 85%)}
.c2{left:570px;background:linear-gradient(120deg,#3c7ea8,#d9c7b0 45%,#c34b4a 80%,#e8d9c9)}
.small{top:855px;width:223px;height:153px}
.small .cap{font-size:19px}
.s1{left:207px;background:linear-gradient(135deg,#5a8f77,#c9c7c0 50%,#6d5f52)}
.s2{left:444px;background:linear-gradient(135deg,#3a3a3a,#e88b2a 50%,#f0b34c)}
.s3{left:681px;background:linear-gradient(135deg,#88703f,#b89a62 50%,#6d6a38)}
.ribbon{position:absolute;left:-30px;top:18px;width:120px;height:20px;background:var(--pink);color:#fff;font-size:10px;text-align:center;line-height:20px;transform:rotate(-45deg)}
.ribbon.violet{background:var(--purple)}
.new{position:absolute;width:44px;height:44px;border-radius:50%;color:#fff;font-size:12px;display:flex;align-items:center;justify-content:center;top:18px;right:10px}
.new.dark{background:#1b2a3a}.new.red{background:#e0182d}.new.blue{background:var(--sky)}

/* lower columns */
.col-h{top:1025px;font-size:14px;padding-bottom:8px;border-bottom:2px dotted #eee}
.post{left:207px;display:flex;gap:6px;font-size:9.5px}
.post .thumb{width:40px;height:36px;border:1px solid #999;background:linear-gradient(135deg,#c7a57d,#7c8ea0)}
.post b{font-weight:400;font-size:10px;display:block;color:#222}
.post span{color:#777;line-height:11px;display:block}
.small-text{font-size:9px;color:#777}
.email{left:468px;top:1093px;width:173px;height:20px;border:1px solid #888;display:flex;align-items:center;font-size:8px;color:#999}
.email i{width:26px;height:18px;background:var(--pink);margin-right:6px}
.subscribe{left:468px;top:1128px;background:var(--pink);color:#fff;font-size:14px;padding:2px 8px}
.contact{left:731px;display:flex;gap:10px;align-items:center;font-size:9px;color:#666;line-height:11px}
.footbar{left:0;top:1165px;width:1111px;height:35px;background:var(--bar);color:#fff;font-size:9px;display:flex;align-items:center;justify-content:space-between;padding:0 207px}
.footbar .here{color:var(--pink)}
</style>
</head>
<body>

<header>
  <div class="abs brand"><span class="brand-dot"></span><span class="brand-name">SaffronMeadowlark</span></div>
  <div class="abs order">Order online<b>0400 555 018</b></div>
  <div class="abs badge24">24h</div>
  <div class="abs account">Register<span>Sign In</span></div>
  <svg class="abs cart" width="32" height="44" viewBox="0 0 32 44"><path d="M9 14V9a7 7 0 0 1 14 0v5" fill="none" stroke="#333" stroke-width="3"/><rect x="2" y="14" width="28" height="28" rx="2" fill="#333"/><circle cx="12" cy="26" r="5" fill="#fff"/><text x="12" y="29" font-size="8" text-anchor="middle" fill="#333">0</text></svg>
</header>

<section>
  <div class="abs hero" role="img" aria-label="Close-up of red organic apples in a wicker basket"></div>
  <nav class="abs nav"><span class="on">Home</span><span>About Us</span><span>Service</span><span>Products</span><span>Blog</span><span>Testimonials</span><span>Contacts</span></nav>
  <div class="abs search"><svg width="25" height="25" viewBox="0 0 25 25"><circle cx="14" cy="11" r="5" fill="none" stroke="#fff" stroke-width="2"/><path d="M10 15l-4 4" stroke="#fff" stroke-width="2.5"/></svg></div>
  <div class="abs halo"></div>
  <div class="abs bubble">
    <p>Organic Produce<br>sourced from, local and<br>intestate farmers deliverd<br>direct to your local pick up location</p>
    <p class="tags">-Organic- -Raw -Wholefoods</p>
    <span class="more">Read more &rarr;</span>
    <div class="dots"><i></i><i></i><i></i><i></i></div>
  </div>
  <div class="abs arrow prev"><svg width="18" height="14" viewBox="0 0 18 14"><path d="M17 7H2M8 1L2 7l6 6" fill="none" stroke="#111" stroke-width="2.4"/></svg></div>
  <div class="abs arrow next"><svg width="18" height="14" viewBox="0 0 18 14"><path d="M1 7h15M10 1l6 6-6 6" fill="none" stroke="#fff" stroke-width="2.4"/></svg></div>
</section>

<section>
  <div class="abs tile t1" role="img" aria-label="Vegetables with a pink overlay">ORGANIC VEGGIES</div>
  <div class="abs tile t2" role="img" aria-label="Shop interior with new arrivals"><span class="label">NEW ARRIVAL</span></div>
  <div class="abs tile t3" role="img" aria-label="Street at night with lit shop fronts"><span class="label">LOCATIONS</span></div>
</section>

<h2 class="abs section-title">New Collection</h2>

<section>
  <div class="abs card big c1" role="img" aria-label="Market stall of fresh organic vegetables and fruit"><div class="cap">Certified Organic Veggies <span>&rarr;</span></div></div>
  <div class="abs card big c2" role="img" aria-label="Children playing with wooden toys"><span class="ribbon violet">ON SALE</span><span class="new blue">NEW</span><div class="cap">Ethical Wooden Toys <span>&rarr;</span></div></div>
  <div class="abs card small s1" role="img" aria-label="Juicer on a kitchen bench"><span class="ribbon">ON SALE</span><span class="new dark">NEW</span><div class="cap">Juicers <span>&rarr;</span></div></div>
  <div class="abs card small s2" role="img" aria-label="Dehydrator trays with dried fruit"><span class="ribbon">ON SALE</span><span class="new red">NEW</span><div class="cap">Dehydrators <span>&rarr;</span></div></div>
  <div class="abs card small s3" role="img" aria-label="Ceramic water filter being filled"><span class="ribbon">ON SALE</span><span class="new blue">NEW</span><div class="cap">Water Fillter <span>&rarr;</span></div></div>
</section>

<section>
  <h3 class="abs col-h" style="left:207px;width:173px;font-weight:400">Latest Blog</h3>
  <div class="abs post" style="top:1061px"><div class="thumb" role="img" aria-label="Family walking"></div><div><b>Parenting</b><span>Lorem ipsum dolor sit amet, consec<br>tetur adipiscin</span></div></div>
  <div class="abs" style="left:207px;top:1107px;width:167px;border-top:1px solid #ccc"></div>
  <div class="abs post" style="top:1119px"><div class="thumb" role="img" aria-label="Pregnant mother"></div><div><b>Pregnancy</b><span>Lorem ipsum dolor sit amet, consec<br>tetur adipiscin</span></div></div>

  <h3 class="abs col-h" style="left:468px;width:173px;font-weight:400">Subscribe to Our Newsletter</h3>
  <p class="abs small-text" style="left:468px;top:1061px">Lorem ipsum dolor sit amet, consectetur adipiscin</p>
  <div class="abs email"><i></i>your@email.com</div>
  <div class="abs subscribe">Subscribe</div>

  <h3 class="abs col-h" style="left:731px;width:176px;font-weight:400">Conatct Us</h3>
  <div class="abs contact" style="top:1059px"><svg width="20" height="22" viewBox="0 0 20 22"><path d="M10 2a5 5 0 0 1 5 5c0 4-5 9-5 9S5 11 5 7a5 5 0 0 1 5-5z" fill="none" stroke="var(--pink)" stroke-width="2"/><path d="M2 20h16" stroke="var(--pink)" stroke-width="2"/></svg><span>Lorem ipsum dolor sit amet conor adipi<br>scin AC 145 BD Fist Flore</span></div>
  <div class="abs contact" style="top:1095px"><svg width="24" height="24" viewBox="0 0 24 24"><circle cx="12" cy="12" r="10" fill="none" stroke="var(--pink)" stroke-width="2"/><text x="12" y="15" font-size="7" text-anchor="middle" fill="var(--pink)">24h</text></svg><span>0400 555 018<br>0400 555 019</span></div>
  <div class="abs contact" style="top:1134px"><svg width="24" height="18" viewBox="0 0 24 18"><rect x="1" y="1" width="22" height="16" fill="none" stroke="var(--pink)" stroke-width="2"/><path d="M1 1l11 9 11-9" fill="none" stroke="var(--pink)" stroke-width="2"/></svg><span>info@saffronmeadowlark.com</span></div>
</section>

<footer class="abs footbar">
  <span><span class="here">Home</span> / About Us / Products / Blog / Testimonials / Contacts</span>
  <span>Copyright © 2014 Saffron Meadowlark All Rights Reserved. Privacy Policy</span>
</footer>

</body>
</html>
```